Business Card Design Project

We need a business card design for an existing company in Dallas/Fort Worth that is expanding services and re-branding. We are changing the name from Brightmoor Commercial Cleaning to Keystride Facility Services. We are expanding from only commercial cleaning to include complete commercial landscape and facility maintenance services, too.

As stated, we offer a package of services that includes landscape, janitorial and facility services, which is largely unique in the industry.

We would like a design that communicates trust/partnership with a professional, corporate image, but not necessarily using the standard white business card. We would like a design that perhaps uses darker blues or perhaps a gray background, but we are open to other ideas. We might also be interested in a double-sided design - maybe with our logo on the back, printed on a gray background?

We will probably stick with the attached logo, but if you've got another inspired idea....

Target Market(s)

Property managers, commercial real estate professionals, corporate executives

Industry/Entity Type

Landscape

Requirements
Should not have
• Not interested in old style fonts.

```html
<!DOCTYPE html>
<html lang="en">
<head>
<meta charset="utf-8">
<title>Keystride Facility Services – Business Card</title>
<link rel="stylesheet" href="https://fonts.googleapis.com/css2?family=Dosis:wght@400;500;600;700&display=swap">
<style>
  :root {
    --page-bg: #e9e6e1;
    --card-white: #fbfbfb;
    --card-dark: #3b3c3e;
    --brand-blue: #1f87c6;
    --ink-dark: #3d3f42;
    --ink-mid: #5a5d61;
    --stripe-gray: #4a4c4f;
    --back-text: #c9cacb;
  }
  * { margin: 0; padding: 0; box-sizing: border-box; }
  html, body {
    width: 1200px; height: 900px; overflow: hidden;
    background: var(--page-bg);
    font-family: "Dosis", sans-serif;
  }
  .sheet {
    width: 1200px; height: 900px;
    display: flex; flex-direction: column; align-items: center; justify-content: center;
    gap: 36px;
  }
  .card {
    position: relative;
    width: 700px; height: 400px;
    overflow: hidden;
    box-shadow: 0 6px 18px rgba(0,0,0,0.18);
  }
  .card-front { background: var(--card-white); }
  .card-back { background: var(--card-dark); }

  .brand {
    position: absolute; left: 40px; top: 48px;
    display: flex; align-items: center; gap: 10px;
  }
  .brand-dot {
    width: 14px; height: 14px; border-radius: 50%; background: var(--brand-blue); flex: none;
  }
  .brand-name {
    font-weight: 600; font-size: 24px; line-height: 1;
    color: var(--ink-dark); white-space: nowrap;
  }

  .person { position: absolute; right: 40px; top: 44px; text-align: right; }
  .person-name { font-size: 30px; font-weight: 700; color: var(--ink-dark); line-height: 1.1; }
  .person-title { font-size: 19px; font-weight: 500; color: var(--brand-blue); margin-top: 4px; }

  .contact {
    position: absolute; left: 40px; top: 212px;
    font-size: 16px; font-weight: 500; color: var(--ink-mid); line-height: 1.4;
  }
  .contact-row { display: flex; align-items: center; gap: 6px; }
  .contact-icon { width: 13px; height: 13px; fill: var(--brand-blue); flex: none; }
  .phone-gap { margin-left: 10px; }

  .band { position: absolute; left: 0; top: 0; width: 700px; height: 400px; }

  .front-url {
    position: absolute; right: 32px; top: 340px;
    font-size: 21px; line-height: 1.2; color: #ffffff; font-weight: 500;
  }
  .front-url b, .back-url b { font-weight: 700; }

  .back-url {
    position: absolute; right: 44px; bottom: 44px;
    font-size: 24px; color: var(--back-text); font-weight: 500;
  }
</style>
</head>
<body>
<main class="sheet">
  <section class="card card-front" aria-label="Front of business card">
    <div class="brand">
      <span class="brand-dot"></span>
      <span class="brand-name">Keystride Facility Services</span>
    </div>

    <div class="person">
      <p class="person-name">Mark Delaney</p>
      <p class="person-title">General Manager</p>
    </div>

    <div class="contact">
      <p>Suit No XYZ, Main Street</p>
      <p>Your City 15, State-County 12345</p>
      <p class="contact-row">
        <svg class="contact-icon" viewBox="0 0 16 16"><path d="M3 1h3l1.5 4-2 1.3a9 9 0 0 0 4.2 4.2L11 8.5l4 1.5v3a2 2 0 0 1-2 2A13 13 0 0 1 1 3a2 2 0 0 1 2-2z"/></svg>
        (123) 456 7890
        <svg class="contact-icon phone-gap" viewBox="0 0 16 16"><rect x="4" y="1" width="8" height="14" rx="1.5"/></svg>
        (123) 456 7890
      </p>
      <p class="contact-row">
        <svg class="contact-icon" viewBox="0 0 16 16"><path d="M1 3h14v10H1z"/><path d="M1 3l7 6 7-6" fill="none" stroke="#fff" stroke-width="1.4"/></svg>
        info@keystridefacilityservices.com
      </p>
    </div>

    <svg class="band" viewBox="0 0 700 400" aria-hidden="true">
      <polygon points="0,316 432,316 420,330 0,330" fill="var(--stripe-gray)"/>
      <polygon points="0,336 418,336 432,322 700,322 700,374 0,374" fill="var(--brand-blue)"/>
    </svg>
    <p class="front-url">www.<b>keystridefacilityservices</b>.com</p>
  </section>

  <section class="card card-back" aria-label="Back of business card">
    <p class="back-url">www.<b>keystridefacilityservices</b>.com</p>
  </section>
</main>
</body>
</html>
```